Business Card and Logo Color Scheme Design Contest

We are starting a new company called Lone Ridge Structural Partners and already have a logo however, the colors for the logo itself are not final and COULD be changed. I'm hoping to move AWAYfrom the gold color in the card and the logo as it seems a bit outdated. What we need help with is to find what our business color scheme will be, and then incorporate those colors into both the logo and the business card design itself. We also want to make sure we are known as "LRS" so in the future we can just refer to ourselves as "LRS" and not Lone Ridge Structural Partners. That being said, I would like to make a slight change to the logo to somehow include the letters "LRS." The logo used in the front of the card design MUST ALSO include the words "Firm No. 64307" within the logo. My vision is for the front of the card to have the information shown in the attached image. For the back of the card, I'm hoping to have something very simple. I'm envisioning a solid color with either the website (www.bridgemarkplans.com) and a simplified version of the logo. I've attached an example but I'm looking for a complete redesign. I'm looking for a slick, modern and simple design.

Industry/Entity Type

Civil Engineer

Contact Information for Business Card

Logo
Firm No. 64307
Marcus Holloway, PE
Chief Operating Officer
Email:mholloway@bridgemarkplans.com
Ph: 936.555.0142 | D: 936.555.0178 | M:210.555.0263
4187 W. Kellingham, Conroe, Texas 77301
www.bridgemarkplans.com

Requirements
Must have
• Logo
Contact Info
Nice to have
• "LRS" Incorporated in the design
Should not have
• The current color scheme

```html
<!DOCTYPE html>
<html lang="en">
<head>
<meta charset="utf-8">
<title>Lone Ridge Structural Partners – Business Card</title>
<link rel="stylesheet" href="https://fonts.googleapis.com/css2?family=Tinos:wght@400;700&display=swap">
<style>
  :root {
    --backdrop: #c5e7dc;
    --card-dark: #1c2836;
    --card-light: #dde4ea;
    --ink-dark: #1c2836;
    --accent-steel: #8fb3cf;
    --text-light: #eef2f5;
    --text-muted: #9fb0c0;
    --rule: #52657a;
    --icon-bg: #6f8aa3;
  }
  * { box-sizing: border-box; margin: 0; padding: 0; }
  html, body { width: 1200px; height: 856px; overflow: hidden; }
  body {
    background: var(--backdrop);
    font-family: "Tinos", "Times New Roman", serif;
    position: relative;
  }
  .card {
    position: absolute;
    border-radius: 30px;
    overflow: hidden;
    box-shadow: 0 10px 26px rgba(30, 60, 50, 0.18);
  }

  /* Back of card */
  .card-back {
    left: 560px; top: 80px;
    width: 540px; height: 309px;
    background: var(--card-light);
  }
  .back-mark {
    position: absolute;
    left: 0; right: 0; top: 88px;
    text-align: center;
    font-size: 58px;
    line-height: 1;
    color: var(--ink-dark);
    letter-spacing: 4px;
  }
  .back-firm {
    position: absolute;
    right: 150px; top: 168px;
    font-size: 13px;
    color: var(--ink-dark);
  }
  .back-band {
    position: absolute;
    left: 0; right: 0; bottom: 34px;
    height: 40px;
    background: var(--ink-dark);
    display: flex; align-items: center; justify-content: center;
    font-size: 16px;
    letter-spacing: 0.5px;
    color: var(--accent-steel);
  }

  /* Front of card */
  .card-front {
    left: 110px; top: 400px;
    width: 660px; height: 377px;
    background: var(--card-dark);
    color: var(--text-light);
  }
  .brand {
    position: absolute;
    left: 56px; top: 52px;
    display: flex; align-items: center; gap: 14px;
  }
  .brand-square {
    width: 46px; height: 46px;
    background: var(--accent-steel);
  }
  .brand-name {
    font-size: 22px;
    line-height: 1.1;
    color: var(--text-light);
    width: 230px;
  }
  .brand-firm {
    position: absolute;
    left: 116px; top: 114px;
    font-size: 13px;
    color: var(--text-light);
  }
  .person {
    position: absolute;
    right: 44px; top: 150px;
    text-align: right;
    width: 290px;
  }
  .person-name {
    font-size: 24px; font-weight: 700;
    color: var(--accent-steel);
  }
  .person-title {
    font-size: 14px;
    color: var(--text-muted);
    border-bottom: 1px solid var(--rule);
    padding-bottom: 3px;
  }
  .divider {
    position: absolute;
    left: 104px; right: 44px; top: 218px;
    border-top: 1px solid var(--rule);
  }
  .contact-list {
    position: absolute;
    left: 380px; top: 224px;
    list-style: none;
    font-size: 14px;
    line-height: 22px;
  }
  .contact-list li { display: flex; align-items: center; gap: 8px; white-space: nowrap; }
  .icon { width: 13px; height: 13px; flex: none; }
  .address {
    position: absolute;
    left: 104px; top: 284px;
    width: 260px;
    border-top: 1px solid var(--rule);
    padding-top: 8px;
    display: flex; gap: 8px;
    font-size: 15px; line-height: 22px;
  }
  .address .icon { margin-top: 4px; }
</style>
</head>
<body>

  <section class="card card-back" aria-label="Card back">
    <div class="back-mark">LRS</div>
    <div class="back-firm">Firm No. 64307</div>
    <div class="back-band">www.bridgemarkplans.com</div>
  </section>

  <section class="card card-front" aria-label="Card front">
    <div class="brand">
      <span class="brand-square"></span>
      <span class="brand-name">Lone Ridge Structural Partners</span>
    </div>
    <div class="brand-firm">Firm No. 64307</div>

    <div class="person">
      <div class="person-name">Marcus Holloway, PE</div>
      <div class="person-title">Chief Operating Officer</div>
    </div>

    <div class="divider"></div>

    <ul class="contact-list">
      <li>
        <svg class="icon" viewBox="0 0 13 13"><rect width="13" height="13" rx="2" fill="#6f8aa3"/><path d="M4 3h2l.6 2-1 .8a5 5 0 0 0 2 2l.8-1 2 .6v2c-4 .3-6.7-2.4-6.4-6.4z" fill="#1c2836"/></svg>
        <span>936.555.0142 | 936.555.0178</span>
      </li>
      <li>
        <svg class="icon" viewBox="0 0 13 13"><rect width="13" height="13" rx="2" fill="#6f8aa3"/><rect x="4" y="2.5" width="5" height="8" rx="1" fill="#1c2836"/></svg>
        <span>210.555.0263</span>
      </li>
      <li>
        <svg class="icon" viewBox="0 0 13 13"><rect width="13" height="13" rx="2" fill="#6f8aa3"/><rect x="2.5" y="4" width="8" height="5.5" fill="#1c2836"/><path d="M2.5 4l4 3 4-3" stroke="#6f8aa3" fill="none"/></svg>
        <span>mholloway@bridgemarkplans.com</span>
      </li>
    </ul>

    <div class="address">
      <svg class="icon" viewBox="0 0 13 13"><rect width="13" height="13" rx="2" fill="#6f8aa3"/><path d="M6.5 2a3 3 0 0 0-3 3c0 2.2 3 5.5 3 5.5s3-3.3 3-5.5a3 3 0 0 0-3-3z" fill="#1c2836"/></svg>
      <span>4187 W. Kellingham, Conroe,<br>Texas 77301</span>
    </div>
  </section>

</body>
</html>
```